Pactwise - Training I Consulting I Review - Related to Contracts/Agreements

We provide legal services, we need a plattform to book video online trainings or local trainings classes and appointments (with calendar feature to select date and see availability at screen), payment over internet, legal document creation over webpage, videos will be produces in the next 3 - 4 moths so this is a place holder item. Participants for the Online trainings shall have a login in area with secured password. Appointments for local trainings and Consulting. Consider Outline in file attached. I can send you also a video with more explanation regarding the purpose.

Target Market(s)

Startup/scale up Software companies that intent to have an international business and need help with their contracts, to sell their products. Sales persons.

Industry/Entity Type

Legal

Coding

Coded - Design and coding required

Number of Pages Required

5+ page

Font styles to use
Serif
Sans Serif

Colors
000000
eeeeee
f5f5f5
ffffff
f8fcfd
3277b5
ecf7fb
cadf82
86cfc6

Requirements
Must have
• See file pactwise attached with outline. Moreover see here first starting point: https://moritz-ebbing.sitebuildr-demo.net/mysite-1 . Main inspiration comes from www.advisoryhub-demo.net from the log in area, see the outline in the file attached with the screen shots. At the end I need someone who can draft the full webpage and maintain it for a yearly fee. It must be simple and well structured layout. Lean. 1st landing page shall not scroll, 2 landing page only a little to see the testimonials and foster of page. There should be a Progress Bar to indicate the booking/selection process. Calendar booking. Easy fast booking.
• I like the colour mix, the feeling and the easy structor of:
• https://www.artpitch-demo.net/design/6374387or
• https://www.artpitch-demo.net/design/6372391 or https://www.artpitch-demo.net/design/6374366
• https://www.agencyfind-demo.net/en/web-design/belgium-be
• https://www.artpitch-demo.net/design/5896857
• https://www.artpitch-demo.net/design/5902173
• https://www.artpitch-demo.net/design/17197349
• https://www.artpitch-demo.net/design/5464461
• https://www.artpitch-demo.net/design/7180908
Nice to have
• page for evaluation and interview, see outline attached in the file with screen shots. Document upload.
Should not have
• many pictures, long scroll down pages on the 1st and 2nd ladding pages, many colours and forms. No need for news letter, search field, no need for links to Chatterly and other social media (except workNet).

```html
<!DOCTYPE html>
<html lang="en">
<head>
<meta charset="UTF-8">
<title>Pactwise – Contract Training, Consulting and Review</title>
<link rel="stylesheet" href="https://fonts.googleapis.com/css2?family=Barlow:wght@400;500&display=swap">
<style>
  :root {
    --ink: #000000;
    --white: #ffffff;
    --band: rgba(238, 238, 238, 0.86);
    --text-dark: #1c1c1c;
    --muted: #6f6f6f;
    --star: #e8c21a;
    --sky-top: #9d9aa6;
    --sky-mid: #b3a6a3;
    --city-left: #3f4a78;
    --city-right: #2f3f8a;
    --floor: #c9c3c9;
  }
  * { box-sizing: border-box; margin: 0; padding: 0; }
  html, body { width: 1200px; height: 646px; overflow: hidden; }
  body { font-family: "Barlow", sans-serif; background: var(--white); }

  .page { position: relative; width: 1200px; height: 646px; overflow: hidden; }

  .hero-backdrop {
    position: absolute; inset: 0 0 37px 0;
    background:
      radial-gradient(ellipse 420px 300px at 560px 170px, rgba(236, 222, 208, 0.75), transparent 70%),
      linear-gradient(90deg, var(--city-left) 0%, rgba(120,120,150,0.55) 22%, rgba(170,160,165,0.35) 45%, rgba(130,110,130,0.45) 70%, var(--city-right) 100%),
      linear-gradient(180deg, var(--sky-top) 0%, var(--sky-mid) 55%, var(--floor) 100%);
  }

  .site-header { position: absolute; top: 0; left: 0; right: 0; height: 80px; }
  .brand {
    position: absolute; left: 103px; top: 6px;
    font-size: 47px; font-weight: 500; color: var(--white); letter-spacing: 0.3px;
  }
  .main-nav {
    position: absolute; left: 445px; top: 30px;
    display: flex; gap: 20px; font-size: 16.5px; color: var(--white);
  }
  .main-nav a { color: inherit; text-decoration: none; }

  .hero-copy { position: absolute; left: 0; right: 0; top: 196px; text-align: center; color: var(--white); }
  .hero-title { font-size: 47px; font-weight: 500; line-height: 1; }
  .hero-services { margin-top: 20px; font-size: 38px; font-weight: 500; line-height: 1; word-spacing: 2px; }
  .hero-services span + span { margin-left: 14px; }
  .enter-button {
    display: inline-block; margin-top: 20px;
    width: 94px; height: 45px; line-height: 43px;
    background: var(--ink); color: var(--white); border: 1px solid var(--white);
    font-size: 22px; font-weight: 500; text-decoration: none;
  }

  .testimonial-band {
    position: absolute; left: 0; right: 0; top: 531px; height: 78px;
    background: var(--band);
  }
  .testimonial-band .arrow { position: absolute; top: 24px; }
  .arrow-prev { left: 87px; }
  .arrow-next { left: 1100px; }
  .quote-mark { position: absolute; left: 119px; top: 26px; }
  .testimonial-text {
    position: absolute; left: 151px; top: 22px; width: 810px;
    font-size: 13.6px; line-height: 21px; color: var(--text-dark);
  }
  .quote-bracket { position: absolute; left: 960px; top: 22px; }
  .reviewer { position: absolute; left: 975px; top: 21px; width: 120px; text-align: center; }
  .reviewer-name { font-size: 16.5px; font-weight: 500; color: var(--text-dark); }
  .reviewer-stars { margin-top: 3px; display: flex; justify-content: center; gap: 4px; }

  .site-footer {
    position: absolute; left: 0; right: 0; bottom: 0; height: 37px;
    background: var(--ink); color: var(--white); font-size: 14px;
  }
  .copyright { position: absolute; left: 105px; top: 9px; }
  .follow { position: absolute; left: 970px; top: 10px; display: flex; align-items: center; gap: 10px; }
  .follow-dot { width: 22px; height: 22px; border-radius: 50%; background: var(--white); }
  .follow-name { font-weight: 500; }
</style>
</head>
<body>
<div class="page">
  <div class="hero-backdrop" role="img" aria-label="Photo of a businessman looking out over city towers through large office windows"></div>

  <header class="site-header">
    <div class="brand">Pactwise</div>
    <nav class="main-nav">
      <a href="#">Home</a>
      <a href="#">Contract Training</a>
      <a href="#">Contract Consulting</a>
      <a href="#">Contract Review</a>
      <a href="#">Reviews</a>
      <a href="#">Team</a>
      <a href="#">Log In</a>
    </nav>
  </header>

  <section class="hero-copy">
    <h1 class="hero-title">We provide legal services</h1>
    <p class="hero-services"><span>Contract Training.</span><span>Contract Consulting.</span><span>Contract Review</span></p>
    <a class="enter-button" href="#">ENTER</a>
  </section>

  <section class="testimonial-band">
    <svg class="arrow arrow-prev" width="14" height="30" viewBox="0 0 14 30"><path d="M12 2 L3 15 L12 28" fill="none" stroke="#555" stroke-width="3"/></svg>
    <svg class="quote-mark" width="19" height="16" viewBox="0 0 19 16"><path d="M0 16V9C0 4 2 1 7 0v3C5 4 4 6 4 8h4v8zM11 16V9c0-5 2-8 7-9v3c-2 1-3 3-3 5h4v8z" fill="#1c1c1c"/></svg>
    <p class="testimonial-text">Lorem ipsum dolor sit amet, consectetuer adipiscing elit, sed diam nonummy nibh euismod tincidunt ut laoreet dolore magna aliquam erat volutpat. Ut wisi enim ad minim veniam, quis nostrud exerci tation</p>
    <svg class="quote-bracket" width="12" height="48" viewBox="0 0 12 48"><path d="M2 2 C8 2 6 20 10 24 C6 28 8 46 2 46" fill="none" stroke="#888" stroke-width="2"/></svg>
    <div class="reviewer">
      <div class="reviewer-name">Lorem Ispum</div>
      <div class="reviewer-stars">
        <svg width="10" height="10" viewBox="0 0 10 10"><path d="M5 0l1.5 3.3 3.5.4-2.6 2.4.7 3.5L5 7.8 1.9 9.6l.7-3.5L0 3.7l3.5-.4z" fill="#e8c21a"/></svg>
        <svg width="10" height="10" viewBox="0 0 10 10"><path d="M5 0l1.5 3.3 3.5.4-2.6 2.4.7 3.5L5 7.8 1.9 9.6l.7-3.5L0 3.7l3.5-.4z" fill="#e8c21a"/></svg>
        <svg width="10" height="10" viewBox="0 0 10 10"><path d="M5 0l1.5 3.3 3.5.4-2.6 2.4.7 3.5L5 7.8 1.9 9.6l.7-3.5L0 3.7l3.5-.4z" fill="#e8c21a"/></svg>
        <svg width="10" height="10" viewBox="0 0 10 10"><path d="M5 0l1.5 3.3 3.5.4-2.6 2.4.7 3.5L5 7.8 1.9 9.6l.7-3.5L0 3.7l3.5-.4z" fill="#e8c21a"/></svg>
        <svg width="10" height="10" viewBox="0 0 10 10"><path d="M5 0l1.5 3.3 3.5.4-2.6 2.4.7 3.5L5 7.8 1.9 9.6l.7-3.5L0 3.7l3.5-.4z" fill="#e8c21a"/></svg>
      </div>
    </div>
    <svg class="arrow arrow-next" width="14" height="30" viewBox="0 0 14 30"><path d="M2 2 L11 15 L2 28" fill="none" stroke="#555" stroke-width="3"/></svg>
  </section>

  <footer class="site-footer">
    <div class="copyright">Copyright © Pactwise . All Rights Reserved</div>
    <div class="follow">
      <span>Follow Us On</span>
      <span class="follow-dot"></span>
      <span class="follow-name">workNet</span>
    </div>
  </footer>
</div>
</body>
</html>
```